business card for a drum shop (musical intsruments)
north ridge beats
Use same font as used in my logo
marcus hollen
4127 Garvey Oakes Ct
Lower Fenwick, Md 20691
marcus.hollen517@quellmail.net
northridgebeats.com
yes, drum image in middle with url at botton
we will upload ai file shortly. please use this for now.

```html
<!DOCTYPE html>
<html lang="en">
<head>
<meta charset="utf-8">
<title>North Ridge Beats – Business Card</title>
<link rel="stylesheet" href="https://fonts.googleapis.com/css2?family=Oswald:wght@300;400&family=Open+Sans:wght@400;700&display=swap">
<style>
  :root {
    --bg: #8c8c8c;
    --ink: #1a1414;
    --paper: #ffffff;
    --muted: #3a3a3a;
    --rule: #c9c9c9;
  }
  * { margin: 0; padding: 0; box-sizing: border-box; }
  html, body { width: 1200px; height: 908px; overflow: hidden; }
  body {
    background: var(--bg);
    font-family: "Open Sans", Arial, sans-serif;
    position: relative;
  }
  .card {
    position: absolute;
    left: 250px;
    width: 700px;
    height: 400px;
    border-radius: 18px;
    overflow: hidden;
  }
  .card--front { top: 44px; background: var(--ink); }
  .card--back { top: 464px; background: var(--paper); }

  /* front */
  .front-mark {
    position: absolute;
    left: 50%; top: 60px;
    transform: translateX(-50%);
    display: flex; flex-direction: column; align-items: center; gap: 18px;
  }
  .front-mark__circle {
    width: 170px; height: 170px; border-radius: 50%;
    background: var(--paper);
  }
  .front-mark__name {
    font-family: "Oswald", Arial, sans-serif;
    font-weight: 300;
    font-size: 26px;
    letter-spacing: 4px;
    text-transform: uppercase;
    color: var(--paper);
  }
  .front-url {
    position: absolute; left: 0; right: 0; bottom: 38px;
    text-align: center;
    color: var(--paper);
    font-size: 18px;
    letter-spacing: 3px;
  }

  /* back */
  .back-brand {
    position: absolute; left: 50px; top: 130px;
    display: flex; align-items: center; gap: 16px;
  }
  .back-brand__circle {
    width: 56px; height: 56px; border-radius: 50%;
    background: var(--ink);
  }
  .back-brand__name {
    font-family: "Oswald", Arial, sans-serif;
    font-weight: 300;
    font-size: 30px;
    line-height: 1.05;
    letter-spacing: 2px;
    text-transform: uppercase;
    color: var(--ink);
    width: 190px;
  }
  .back-divider {
    position: absolute; left: 340px; top: 40px;
    width: 1px; height: 190px; background: var(--rule);
  }
  .contact {
    position: absolute; left: 362px; top: 50px;
    color: var(--muted);
  }
  .contact__name {
    font-weight: 700; font-size: 22px; color: var(--ink);
    margin-bottom: 16px;
  }
  .contact__line { font-size: 14px; line-height: 1.6; display: flex; align-items: center; gap: 7px; }
  .contact__line svg { width: 14px; height: 14px; flex: none; }
  .back-wave { position: absolute; left: 0; bottom: 0; width: 700px; height: 170px; }
  .back-url {
    position: absolute; right: 36px; bottom: 22px;
    color: var(--paper);
    font-size: 17px; font-weight: 700; letter-spacing: 1px;
  }
</style>
</head>
<body>
  <section class="card card--front">
    <div class="front-mark">
      <div class="front-mark__circle"></div>
      <div class="front-mark__name">north ridge beats</div>
    </div>
    <p class="front-url">www.northridgebeats.com</p>
  </section>

  <section class="card card--back">
    <div class="back-brand">
      <div class="back-brand__circle"></div>
      <div class="back-brand__name">north ridge beats</div>
    </div>
    <div class="back-divider"></div>
    <div class="contact">
      <h1 class="contact__name">Marcus Hollen</h1>
      <p class="contact__line">4127 Garvey Oakes Ct</p>
      <p class="contact__line">Lower Fenwick, Md 20691</p>
      <p class="contact__line">
        <svg viewBox="0 0 16 16" aria-hidden="true"><circle cx="8" cy="8" r="7" fill="none" stroke="currentColor" stroke-width="1.2"/><path d="M5.5 4.5l1.5 0 .6 2-1 .8a5 5 0 0 0 2 2l.8-1 2 .6v1.5c-3.5.3-6.2-2.4-5.9-5.9z" fill="currentColor"/></svg>
        301-555-0148
      </p>
      <p class="contact__line">
        <svg viewBox="0 0 16 16" aria-hidden="true"><circle cx="8" cy="8" r="7" fill="none" stroke="currentColor" stroke-width="1.2"/><rect x="4" y="5.5" width="8" height="5" fill="none" stroke="currentColor" stroke-width="1"/><path d="M4 5.5l4 3 4-3" fill="none" stroke="currentColor" stroke-width="1"/></svg>
        marcus.hollen517@quellmail.net
      </p>
    </div>
    <svg class="back-wave" viewBox="0 0 700 170" preserveAspectRatio="none" aria-hidden="true">
      <path d="M0 150 C200 150 380 120 520 60 C600 25 660 10 700 8 L700 170 L0 170 Z" fill="var(--ink)"/>
      <path d="M0 138 C210 136 380 104 515 44 C595 10 655 -4 700 -6" fill="none" stroke="var(--ink)" stroke-width="3"/>
    </svg>
    <p class="back-url">www.northridgebeats.com</p>
  </section>
</body>
</html>
```